Website Design - for Energy Efficiency company - large corporate feel

Hi there,
Thanks for checking out this project!
We're a UK based energy efficiency business. We arrange for energy efficient systems to be fitted in people's houses (i.e. efficient boilers, solar panels etc.) However, we do not install them ourselves as we have accredited installers who install on our behalf. Therefore the website should appeal to these businesses and have a very professional corporate feel. The final design should communicate that we are a financially safe large corporation.
Our existing website should not be used for inspiration as the style and content are very outdated (it was from a time when were installers - which we no longer are).
The new website design should use the greens from our logo, however I don't want the site saturated in this colour.
I'm really open to your chosen layout and therefore I'm not a huge fan of including links to websites I like - as I don't want to limit your own creativity. However, I would like it to look corporate (but not too boring and unimaginative).
So here's a few links to websites that I feel give a feel of financially safe / large corporate etc. Although you certainly don't have to design with this style / layout in mind:
http://www.brelvanhub.org.uk/advice
http://www.tolvenrise.co.uk/
http://www.qpwd.org.uk/
http://www.wendrowkeyplot.co.uk/
http://www.ruvasto.co.uk/ (very bad design but looks corporate)
http://www.pellarwatt.org.uk/
http://www.vq.co.uk/ (looks corporate but too busy and boring)
http://www.quellisto.co.uk/business/index.htm
http://www.dormavel.com/
https://www.ostrevan.com/en/index.html
The site is for 4 different audiences:
Consumers | Businesses | Public Sector | Installers
Therefore, it's important that there is some form of way of splitting the site up into these sections (almost like 4 websites in 1). Each section will then have the navigation menu with 7 links.
I've attached our logo (company-logo.jpg) and another logo design we have to display inline with regulations (blue-pact-logo.jpg).
Happy designing, and thank you!

```html
<!DOCTYPE html>
<html lang="en">
<head>
<meta charset="utf-8">
<title>Leafmoor Energy</title>
<link rel="stylesheet" href="https://fonts.googleapis.com/css2?family=Arimo:wght@400&family=Bitter:wght@400;600&family=Open+Sans:wdth,wght@75..100,300..800&display=swap">
<style>
:root{
  --green:#8cc63e;
  --green-light:#a3d355;
  --green-dark:#6ea02a;
  --green-ink:#2f4a10;
  --nav-ink:#3d5a18;
  --page:#f4f4f4;
  --text:#4a4a4a;
  --footer:#1c1c1c;
  --footer-line:#3a3a3a;
  --footer-text:#bdbdbd;
  --white:#ffffff;
}
*{margin:0;padding:0;box-sizing:border-box}
html,body{width:1050px;height:1200px;overflow:hidden}
body{position:relative;background:var(--page);font-family:"Open Sans",Arial,sans-serif;color:var(--text)}
.topline{position:absolute;left:0;top:0;width:1050px;height:3px;background:var(--green)}
.subbar{position:absolute;left:0;top:40px;width:1050px;height:27.5px;background:var(--white)}
.mainnav{position:absolute;left:399px;top:2.5px;right:0;height:37.5px;background:linear-gradient(var(--green-light),var(--green));display:flex}
.mainnav a{display:block;padding:0 10px;line-height:37.5px;font-size:11px;color:var(--nav-ink);text-decoration:none;text-transform:uppercase;border-right:1px solid rgba(0,0,0,.12)}
.mainnav a.is-active{background:rgba(0,0,0,.1)}
.brand{position:absolute;left:159px;top:0;width:240px;height:87.5px;background:var(--white);display:flex;align-items:center;padding-left:14px;gap:10px;z-index:3}
.brand-dot{width:38px;height:38px;border-radius:50%;background:var(--green);flex:none}
.brand-name{font-size:22px;font-weight:700;color:var(--green-dark);line-height:1}
.callus{position:absolute;left:407px;top:47px;font-size:11.5px;color:var(--green-ink)}
.quote{position:absolute;left:700px;width:192px;top:46px;text-align:right;font-size:12.5px;font-weight:700;color:var(--green-dark);text-transform:uppercase}
.hero{position:absolute;left:0;top:67.5px;width:1050px;height:327.5px;background:linear-gradient(160deg,#cfd3d6 0%,#8f9aa8 30%,#3b4f7a 55%,#c9cdd0 100%)}
.hero-caption{position:absolute;left:159px;top:255px;width:734px;height:67.5px;background:rgba(255,255,255,.85);border-radius:4px 4px 0 0;text-align:center;padding-top:6px}
.hero-title{font-family:"Bitter",Georgia,serif;font-weight:600;font-size:32px;color:var(--green-ink);line-height:1.1}
.hero-sub{font-family:"Bitter",Georgia,serif;font-size:13.5px;color:#222;margin-top:4px}
.hero-tabs{position:absolute;left:159px;top:322.5px;width:734px;height:44px;display:flex;background:linear-gradient(var(--green-light),var(--green-dark));border-radius:0 0 3px 3px}
.hero-tab{display:flex;align-items:center;justify-content:center;gap:14px;color:var(--white);font-size:15px;border-right:1px solid rgba(255,255,255,.3)}
.hero-tab:last-child{border-right:0}
.hero-tab svg{width:30px;height:30px}
.estimate{position:absolute;left:159px;top:397.5px;width:734px;height:49px;background:var(--green);border-radius:3px}
.estimate-label{position:absolute;left:12px;top:3px;font-size:23px;font-weight:800;font-stretch:75%;line-height:21px;color:var(--green-ink);text-transform:uppercase}
.estimate-field{position:absolute;top:11px;width:165px;height:27.5px;background:var(--white);border-radius:2px;font-size:11.5px;color:#555;line-height:27.5px;padding-left:9px}
.estimate-go{position:absolute;left:679px;top:3px;width:43px;height:43px;border-radius:50%;background:var(--white);font-size:22px;font-weight:800;color:var(--green-ink);text-align:center;line-height:43px}
.audience{position:absolute;width:360px;height:157.5px;border-radius:3px;overflow:hidden}
.audience-photo{height:105px}
.audience-label{height:52.5px;background:var(--green);color:var(--green-ink);font-size:41px;letter-spacing:-2px;padding-left:10px;line-height:52.5px}
.intro{position:absolute;left:157.5px;top:817px;width:736px;font-size:10.2px;line-height:13.4px;color:#333;text-align:justify}
.intro p+p{margin-top:13px}
.footer{position:absolute;left:0;top:962.5px;width:1050px;height:237.5px;background:var(--footer)}
.f-brand{position:absolute;left:159px;top:22px;display:flex;align-items:center;gap:8px}
.f-brand-dot{width:28px;height:28px;border-radius:50%;background:var(--green);flex:none}
.f-brand-name{font-size:17px;font-weight:700;color:var(--green);line-height:1;white-space:nowrap}
.f-badge{position:absolute;left:225px;top:66px;width:48px;height:52px;background:var(--white);border:2px solid var(--green-dark)}
.f-links{position:absolute;left:381px;top:25px;list-style:none;font-family:"Arimo",Arial,sans-serif;font-size:10px;line-height:15px;color:var(--footer-text)}
.f-head{position:absolute;top:19px;font-size:13px;font-weight:400;color:var(--white)}
.f-text{position:absolute;top:42px;font-family:"Arimo",Arial,sans-serif;font-size:9.5px;line-height:15px;color:var(--footer-text)}
.f-text .hl{color:var(--green)}
.f-time{display:block;font-size:8px;color:#fff}
.f-rule{position:absolute;left:157.5px;top:131px;width:736px;height:1px;background:var(--footer-line)}
.f-copy{position:absolute;left:157.5px;top:143px;font-family:"Arimo",Arial,sans-serif;font-size:9.5px;color:var(--footer-text)}
.f-social{position:absolute;left:779px;top:136px;display:flex;gap:7.5px}
.f-social span{width:22.5px;height:22.5px;background:var(--green)}
.f-skyline{position:absolute;left:0;top:181px;width:1050px;height:56.5px;background:linear-gradient(transparent,#2c2c2c 60%)}
</style>
</head>
<body>
<div class="topline"></div>
<div class="subbar"></div>
<nav class="mainnav">
  <a class="is-active">Home</a><a>About Us</a><a>Blue Pact</a><a>Eco</a><a>Landlords</a><a>Renewables</a><a>Contact Us</a>
</nav>
<div class="brand"><span class="brand-dot"></span><span class="brand-name">LEAFMOOR ENERGY</span></div>
<div class="callus">CALL US :&nbsp; 020 7946 0321</div>
<div class="quote">Get a free quote</div>

<div class="hero" role="img" aria-label="Workers fitting solar panels on a flat roof"></div>
<div class="hero-caption">
  <h1 class="hero-title">Lorem ipsum dolor sit amet</h1>
  <p class="hero-sub">Lorem ipsum dolor sit amet, consectetudLorem ipsum dolor sit amet, consectetudipiscing elit.</p>
</div>
<div class="hero-tabs">
  <div class="hero-tab" style="width:211px"><svg viewBox="0 0 30 30"><path d="M3 20h22M6 17l16-6 3 2-15 7z" fill="none" stroke="#fff" stroke-width="2"/></svg>Moving in the UK?</div>
  <div class="hero-tab" style="width:174px"><svg viewBox="0 0 30 30"><circle cx="15" cy="15" r="11" fill="#fff"/></svg>Blue Pact</div>
  <div class="hero-tab" style="width:171px"><svg viewBox="0 0 30 30"><path d="M5 7h20v12H5zM5 11h20M5 15h20M12 7v12M18 7v12M15 19v5M10 24h10" fill="none" stroke="#fff" stroke-width="1.6"/></svg>Renewables</div>
  <div class="hero-tab" style="width:178px"><svg viewBox="0 0 30 30"><path d="M6 18v-4a9 9 0 0 1 18 0v4" fill="none" stroke="#fff" stroke-width="2"/><rect x="4" y="16" width="5" height="8" rx="2" fill="#fff"/><rect x="21" y="16" width="5" height="8" rx="2" fill="#fff"/></svg>24/7&nbsp; Support</div>
</div>

<form class="estimate">
  <div class="estimate-label">Free<br>Estimate</div>
  <div class="estimate-field" style="left:157.5px">Your Name...</div>
  <div class="estimate-field" style="left:330px">Phone...</div>
  <div class="estimate-field" style="left:504px">Email...</div>
  <div class="estimate-go">GO</div>
</form>

<section class="audience" style="left:157.5px;top:466px">
  <div class="audience-photo" role="img" aria-label="Family relaxing together on a sofa at home" style="background:linear-gradient(120deg,#eae6e0,#cdb8a2)"></div>
  <div class="audience-label">Consumers</div>
</section>
<section class="audience" style="left:534px;top:466px">
  <div class="audience-photo" role="img" aria-label="Business team meeting around documents" style="background:linear-gradient(120deg,#5d6d66,#26312e)"></div>
  <div class="audience-label">Businesses</div>
</section>
<section class="audience" style="left:157.5px;top:640px">
  <div class="audience-photo" role="img" aria-label="Many raised hands" style="background:linear-gradient(90deg,#ffffff,#e8c6a8 50%,#ffffff)"></div>
  <div class="audience-label">Public Sector</div>
</section>
<section class="audience" style="left:534px;top:640px">
  <div class="audience-photo" role="img" aria-label="Installer in hard hat holding a solar panel" style="background:linear-gradient(90deg,#9b5a32,#c98a55 60%,#54627a)"></div>
  <div class="audience-label">Installers</div>
</section>

<div class="intro">
  <p>Lorem ipsum dolor sit amet, consectetuer adipiscing elit. Aenean commodo ligula eget dolor. Aenean massa. Cum sociis natoque penatibus et magnis dis parturient montes, nascetur ridiculus mus. Donec quam felis, ultricies nec, pellentesque eu, pretium quis, sem. Nulla consequat massa quis enim. Donec pede justo, fringilla vel, aliquet nec, vulputate eget, arcu. In enim justo, rhoncus ut, imperdiet a, venenatis vitae, justo. Nullam dictum felis eu pede mollis pretium. Donec quam felis, ultricies nec, pellentesque eu, pretium quis, sem. Nulla consequat massa quis enim. Donec pede justo, fringilla vel,</p>
  <p>aliquet nec, vulputate eget, arcu. In enim justo, rhoncus ut, imperdiet a, venenatis vitae, justo. Nullam dictum felis eu pede mollis pretium. Integer tincidunt. Cras dapibus. Vivamus elementum semper nisi. Aenean vulputate eleifend tellus. Aenean leo ligula, porttitor eu, consequat vitae, eleifend ac, enim. Aliquam lorem ante, Nullam dictum felis eu pede mollis pretium. Integer tincidunt. Cras dapibus. Vivamus elementum semper nisi.</p>
</div>

<footer class="footer">
  <div class="f-brand"><span class="f-brand-dot"></span><span class="f-brand-name">LEAFMOOR ENERGY</span></div>
  <div class="f-badge" role="img" aria-label="Accreditation badge"></div>
  <ul class="f-links"><li>Home</li><li>About Us</li><li>Blue Pact</li><li>ECO</li><li>Landlords</li><li>Renewables</li></ul>
  <h3 class="f-head" style="left:511px">@leafmoorenergy</h3>
  <p class="f-text" style="left:511px;width:185px">Lorem ipsum dolor sit amet,parturient montes." consectetparturient montes."parturi-ent montes."uer <span class="hl">@adipiscing elit. #Aenean</span><span class="f-time">2mins ago</span></p>
  <h3 class="f-head" style="left:742px">Contact Us</h3>
  <p class="f-text" style="left:741px;width:155px;color:#8a8a8a">Lorem ipsum dolor sit amet,parturi-ent montes." consectetparturient montes."parturient montes."uer</p>
  <div class="f-rule"></div>
  <p class="f-copy">Copyright © 2013 Leafmoor Energy &nbsp;|&nbsp; Terms of Service &nbsp;|&nbsp; Sitemap</p>
  <div class="f-social"><span></span><span></span><span></span><span></span></div>
  <div class="f-skyline" role="img" aria-label="City skyline silhouette"></div>
</footer>
</body>
</html>
```